Professional Business Card for Luxury Hotel & Resort Development Firm. Advisory firm

Project Overview: We are a specialized advisory firm focused on Hotel & Resort Development. Our clients are high-net-worth investors and major hospitality brands.

Design Requirements:

Style: Minimalist, sophisticated, and trustworthy. We want to avoid looking too "corporate" or "dry"—it should feel premium.

Key Elements: Please incorporate our logo [もしロゴがあれば] and emphasize a clean layout with plenty of white space.

Color Palette: We prefer Grey and White or Black and White to evoke a sense of luxury and stability.

Typography: Professional garamond, or sans-serif or elegant serif fonts

Goal: The card should feel substantial and high-end when handed to a client, reflecting our expertise in multi-million dollar developments.
Updates

I am currently on a business trip for field research and have limited access to my desktop. Additionally, I have just provided detailed technical feedback to a designer and am waiting for their refined proposals. To ensure the final logo meets the high standards of my new advisory firm, I would like to extend the deadline by 7 days. Thank you for your support.

Target Market(s)

High-net-worth investors, luxury hospitality brands, and real estate developers.

Contact Information for Business Card

Firm Name: Harbor Crest Partners, My Name: Kenji Morisawa, Title: Founder, Address 5-8-4 Kitanomura Aoba Yokohama Japan 225-0143, email address: kmorisawa@harborcrestpx.example, Tel: +81 90-4183-2750. Front Site (Primary): Japanese translation of the back side, Please use a clean Japanese font (like Mincho) that complements the Garmond on the English side Back side: English. Note for Japanese text: since the frond side is the main fae, please ensure the layout is clean and professional. Please use a high-quality Mincho ( Serif-style) font for Japanese to mach the Garmond used on the English side. Text for Front side (Japanese) Harbor Crest Partners, 役職:代表、森沢健二、225-0143 横浜市青葉区北野村5-8-4. Name of the firm can stay in English.

Font styles to use
Other font styles liked:
• Font Preference: Please use Garamond for all text to maintain a consistent, elegant, and classic professional look.

Requirements
Must have
• Professional and clean layout, high-end feel.
Nice to have
• Minimalist design with subtle luxury accents.

```html
<!DOCTYPE html>
<html lang="ja">
<head>
<meta charset="utf-8">
<title>Harbor Crest Partners — Business Card</title>
<link href="https://fonts.googleapis.com/css2?family=EB+Garamond:wght@400;500&family=Shippori+Mincho:wght@400;500&family=Montserrat:wght@500&display=swap" rel="stylesheet">
<style>
  :root {
    --page: #ffffff;
    --card-deep: #000000;
    --card-mid: #1e1e1e;
    --card-sheen: #666666;
    --card-edge: #4a4a4a;
    --silver-light: #f2f2f2;
    --silver-mid: #bdbdbd;
    --silver-dark: #7a7a7a;
    --rule: #9a9a9a;
  }
  * { margin: 0; padding: 0; box-sizing: border-box; }
  html, body {
    width: 1200px; height: 1200px; overflow: hidden;
    background: var(--page);
  }
  .canvas { position: relative; width: 1200px; height: 1200px; }

  .card {
    position: absolute;
    width: 569px; height: 342px;
    background: linear-gradient(to top right,
      var(--card-deep) 0%, var(--card-mid) 45%, #333 66%,
      var(--card-sheen) 82%, var(--card-edge) 100%);
    box-shadow: 4px 5px 8px rgba(0,0,0,0.35);
    color: var(--silver-mid);
  }
  .card--front { left: 181px; top: 253px; }
  .card--back  { left: 457px; top: 612px; }

  .silver {
    background: linear-gradient(100deg, var(--silver-light) 0%, var(--silver-mid) 45%, var(--silver-dark) 100%);
    -webkit-background-clip: text; background-clip: text;
    color: transparent;
  }

  .centered { position: absolute; left: 0; right: 0; text-align: center; transform: translateY(-50%); }

  .firm-name {
    top: 49px;
    font-family: "EB Garamond", serif;
    font-size: 20px; letter-spacing: 2px;
  }
  .front-rule {
    position: absolute; left: 98px; width: 375px; top: 63px; height: 1px;
    background: linear-gradient(90deg, transparent, var(--silver-light) 50%, transparent);
  }
  .jp-name {
    top: 132px;
    font-family: "Shippori Mincho", serif;
    font-size: 60px; letter-spacing: 2px; line-height: 1;
  }
  .jp-title {
    top: 190px;
    font-family: "Shippori Mincho", serif;
    font-size: 30px; letter-spacing: 2px;
  }
  .jp-postal {
    top: 258px;
    font-family: "EB Garamond", serif;
    font-size: 21px; letter-spacing: 1.5px;
  }
  .jp-address {
    top: 289px;
    font-family: "Shippori Mincho", serif;
    font-size: 21px; letter-spacing: 1.5px; color: var(--silver-mid);
  }

  .identity { position: absolute; left: 49px; width: 230px; text-align: center; }
  .en-name {
    position: absolute; left: 0; right: 0; top: 157px; transform: translateY(-50%);
    font-family: "EB Garamond", serif; font-size: 27px; letter-spacing: 1px; white-space: nowrap;
  }
  .back-rule {
    position: absolute; left: 0; right: 0; top: 175px; height: 1px;
    background: linear-gradient(90deg, transparent, var(--silver-light) 50%, transparent);
  }
  .en-title {
    position: absolute; left: 0; right: 0; top: 187px; transform: translateY(-50%);
    font-family: "Montserrat", sans-serif; font-size: 10px; color: #d6d6d6;
  }
  .divider { position: absolute; left: 296px; top: 103px; width: 1px; height: 141px; background: var(--rule); }

  .contact {
    position: absolute; left: 309px;
    font-family: "EB Garamond", serif; font-size: 12.5px; line-height: 14px;
    color: var(--silver-mid); white-space: nowrap;
  }
  .contact--phone { top: 117px; color: #a0a0a0; }
  .contact--email { top: 149px; color: #a0a0a0; font-size: 12px; }
  .contact--address { top: 187px; color: #c8c8c8; }
</style>
</head>
<body>
<main class="canvas">
  <section class="card card--front" aria-label="Front, Japanese">
    <p class="centered firm-name silver">Harbor Crest Partners</p>
    <div class="front-rule"></div>
    <h1 class="centered jp-name silver">森沢健二</h1>
    <p class="centered jp-title silver">代表</p>
    <p class="centered jp-postal silver">225-0143</p>
    <p class="centered jp-address">横浜市青葉区北野村5-8-4</p>
  </section>

  <section class="card card--back" aria-label="Back, English">
    <div class="identity" style="top:0;height:100%;">
      <h2 class="en-name silver">Kenji Morisawa</h2>
      <div class="back-rule"></div>
      <p class="en-title">Founder</p>
    </div>
    <div class="divider"></div>
    <p class="contact contact--phone">+81 90-4183-2750</p>
    <p class="contact contact--email">kmorisawa@harborcrestpx.example</p>
    <p class="contact contact--address">5-8-4 Kitanomura<br>Aoba,Yokohama<br>Japan 225-0143</p>
  </section>
</main>
</body>
</html>
```